A simple and smart interface for busy teachers

We have an existing app (hybrid) on Apple Appstore and Google Playstore that we wish to refresh with some awesome designs and simplified screens.

We would like to stick to our existing colour scheme, see our website plovano.co.nz or screenshots on the appstore for more details and use of colours.

The uploaded files are current screens that we would like redesigned. Specifically, here are additional thoughts on what we wish to see:
1. With the Active Jobs screen, we would prefer to see a week-ly calendar style layout.
2. With Favourites, we would like to see each person's availability going across the page.

Target Market(s)

Middle aged women. (40+). New to tech users.

Industry/Entity Type

Education

Number of Pages Required

5+ page

Font styles to use
Sans Serif

Colors
ec1f27
474747
f78f20

Requirements
Must have
• Calendar view.
• Tidy and sharp info about the jobs.
Nice to have
• Simple and sharp.
Should not have
• Complicated graphics.
• Cluttered designs.
• Too much red. Screens should be mainly white(ish) with red and black.

```html
<!DOCTYPE html>
<html lang="en">
<head>
<meta charset="utf-8">
<title>Job Detail – Q&amp;A</title>
<link rel="stylesheet" href="https://fonts.googleapis.com/css2?family=Roboto+Condensed:wght@400;700&family=Arimo:wght@700&display=swap">
<style>
  :root {
    --brand-red: #ec1f27;
    --bubble-red: #c93022;
    --bubble-grey: #ececec;
    --ink: #1c1c1c;
    --meta-grey: #8c8c8c;
    --meta-light: #e8e3e2;
    --page: #ffffff;
    --composer: #ececec;
  }
  * { box-sizing: border-box; margin: 0; padding: 0; }
  html, body { width: 725px; height: 1200px; overflow: hidden; background: var(--page); }
  body { position: relative; font-family: "Roboto Condensed", Arial, sans-serif; color: var(--ink); }

  .app-bar { position: absolute; left: 3px; top: 0; width: 722px; height: 124px; background: var(--brand-red); }
  .app-bar__title { position: absolute; left: 0; right: 0; top: 34px; text-align: center; font-family: "Arimo", Arial, sans-serif; font-weight: 700; font-size: 49px; color: #fff; padding-left: 4px; }
  .app-bar__icon { position: absolute; }

  .intro { position: absolute; left: 60px; right: 60px; top: 124px; text-align: center; font-size: 26px; line-height: 40px; padding-top: 5px; }

  .thread { position: absolute; left: 0; top: 0; width: 725px; height: 982px; overflow: hidden; }
  .bubble { position: absolute; border-radius: 9px; padding: 10px 9px 0 10px; font-size: 30px; line-height: 40px; }
  .bubble__meta { font-size: 26px; line-height: 40px; }
  .bubble__meta b { font-weight: 700; }
  .bubble--school { background: var(--bubble-red); color: #fff; text-align: right; left: 112px; width: 538px; }
  .bubble--school .bubble__meta { color: var(--meta-light); }
  .bubble--school::after { content: ""; position: absolute; right: -13px; bottom: 8px; border-left: 14px solid var(--bubble-red); border-top: 12px solid transparent; border-bottom: 14px solid transparent; }
  .bubble--candidate { background: var(--bubble-grey); left: 76px; }
  .bubble--candidate .bubble__meta { color: var(--meta-grey); }
  .bubble--candidate::before { content: ""; position: absolute; left: -10px; bottom: 10px; border-right: 11px solid var(--bubble-grey); border-top: 22px solid transparent; }

  .composer { position: absolute; left: 5px; top: 982px; width: 720px; height: 99px; background: var(--composer); }
  .composer__field { position: absolute; left: 33px; top: 16px; width: 536px; height: 83px; background: #fff; border: 1px solid #e2e2e2; border-bottom: none; font-size: 27px; color: #9a9a9a; padding: 8px 10px; }
  .composer__send { position: absolute; left: 585px; top: 19px; width: 103px; height: 76px; background: var(--bubble-red); border: 1px solid #a8261c; border-radius: 3px; color: #fff; font-size: 36px; text-align: center; line-height: 74px; }

  .tab-bar { position: absolute; left: 2px; top: 1081px; width: 723px; height: 119px; background: var(--brand-red); }
  .tab { position: absolute; top: 0; width: 200px; height: 119px; text-align: center; color: #fff; }
  .tab svg { position: absolute; top: 12px; left: 50%; transform: translateX(-50%); }
  .tab__label { position: absolute; left: 0; right: 0; bottom: 8px; font-family: "Arimo", Arial, sans-serif; font-weight: 700; font-size: 29px; }
</style>
</head>
<body>
  <header class="app-bar">
    <svg class="app-bar__icon" style="left:26px;top:35px" width="40" height="54" viewBox="0 0 40 54" aria-label="Back">
      <path d="M36 2 Q38 0 38 4 L38 50 Q38 54 35 52 L3 30 Q0 27 3 24 Z" fill="#fff"/>
    </svg>
    <h1 class="app-bar__title">Job Detail</h1>
    <svg class="app-bar__icon" style="left:525px;top:33px" width="62" height="62" viewBox="0 0 62 62" aria-label="Settings">
      <g fill="#fff" transform="translate(31 31)">
        <rect x="-6" y="-30" width="12" height="60" rx="3"/>
        <rect x="-6" y="-30" width="12" height="60" rx="3" transform="rotate(45)"/>
        <rect x="-6" y="-30" width="12" height="60" rx="3" transform="rotate(90)"/>
        <rect x="-6" y="-30" width="12" height="60" rx="3" transform="rotate(135)"/>
        <circle r="21"/>
      </g>
      <circle cx="31" cy="31" r="9" fill="var(--brand-red)"/>
    </svg>
    <svg class="app-bar__icon" style="left:617px;top:33px" width="74" height="57" viewBox="0 0 74 57" aria-label="Home">
      <path d="M37 0 L74 31 L64 31 L64 57 L45 57 L45 40 L29 40 L29 57 L10 57 L10 31 L0 31 Z" fill="#fff"/>
    </svg>
  </header>

  <main class="thread">
    <p class="intro">Send message to all invited candidates. Use Q&amp;A to tell them about last-minute changes, and to answer their questions.</p>

    <div class="bubble bubble--school" style="top:285px;height:141px">
      <p>We have a teacher aide assisting in this classroom.</p>
      <p class="bubble__meta"><b>School</b>, 14 hours ago</p>
    </div>

    <div class="bubble bubble--candidate" style="top:447px;width:538px;height:141px">
      <p>Has the regular teacher left any activities for the students?</p>
      <p class="bubble__meta"><b>Reid Halloway</b>, 13 hours ago</p>
    </div>

    <div class="bubble bubble--candidate" style="top:609px;width:466px;height:100px">
      <p>What is parking like at your school?</p>
      <p class="bubble__meta"><b>Mirela Tosk</b>, 13 hours ago</p>
    </div>

    <div class="bubble bubble--school" style="top:730px;height:141px">
      <p>Plenty of street parking nearby. Please do not park in the staff carpark.</p>
      <p class="bubble__meta"><b>School</b>, 13 hours ago</p>
    </div>

    <div class="bubble bubble--candidate" style="top:893px;width:538px;height:141px">
      <p>How many students are there in the class?</p>
      <p class="bubble__meta"><b>Reid Halloway</b>, 12 hours ago</p>
    </div>
  </main>

  <form class="composer">
    <div class="composer__field">Message Here</div>
    <div class="composer__send">Send</div>
  </form>

  <nav class="tab-bar">
    <div class="tab" style="left:21px">
      <svg width="58" height="58" viewBox="0 0 58 58" aria-hidden="true">
        <circle cx="29" cy="29" r="29" fill="#fff"/>
        <circle cx="30" cy="15" r="5" fill="var(--brand-red)"/>
        <path d="M21 24 H34 V42 H38 V48 H21 V42 H25 V30 H21 Z" fill="var(--brand-red)"/>
      </svg>
      <span class="tab__label">INFO</span>
    </div>
    <div class="tab" style="left:261px">
      <svg width="84" height="62" viewBox="0 0 84 62" aria-hidden="true">
        <g fill="#fff">
          <circle cx="42" cy="14" r="14"/>
          <circle cx="15" cy="21" r="9"/>
          <circle cx="69" cy="21" r="9"/>
          <path d="M0 44 Q0 34 9 34 L21 34 Q20 40 20 46 L20 62 L4 62 Q0 62 0 58 Z"/>
          <path d="M84 44 Q84 34 75 34 L63 34 Q64 40 64 46 L64 62 L80 62 Q84 62 84 58 Z"/>
          <path d="M24 44 Q24 32 34 32 L50 32 Q60 32 60 44 L60 62 L24 62 Z"/>
        </g>
      </svg>
      <span class="tab__label">Candidates</span>
    </div>
    <div class="tab" style="left:509px">
      <svg width="60" height="58" viewBox="0 0 60 58" aria-hidden="true">
        <path d="M10 0 H50 Q60 0 60 10 V32 Q60 40 56 42 L56 58 L40 44 H10 Q0 44 0 34 V10 Q0 0 10 0 Z" fill="#fff"/>
      </svg>
      <span class="tab__label">Q&amp;A</span>
    </div>
  </nav>
</body>
</html>
```